Business Card Design

The name of my business is called Brisk Lantern, Inc.

We are the first brick and mortar store in our state that will specialize in spy equipment. I don't want the term "spy equipment" used in the design of the card. I would like a double sided card with the one side having all my contact information and the other side having the company name and the quote "Discreet Surveillance Equipment". I'm not looking for the perfect card on the first try but am not looking to make many changes.

I would like the card to speak sophistication so I tend to lean toward dark color backgrounds.

Industry/Entity Type

Store

Contact Information for Business Card

Harold Dumbrell, Consultant
555-318-0927
harold.dumbrell@brisklantern.example
www.brisklantern.example

```html
<!DOCTYPE html>
<html lang="en">
<head>
<meta charset="utf-8">
<title>Brisk Lantern, Inc. – Business Card</title>
<link rel="stylesheet" href="https://fonts.googleapis.com/css2?family=Questrial&family=Mulish:ital,wght@0,400;0,700;1,400&display=swap">
<style>
  :root {
    --card-red: #8a161e;
    --card-black: #000000;
    --card-white: #ffffff;
    --page-bg: #ffffff;
    --card-shadow: rgba(0, 0, 0, 0.45);
  }
  * { margin: 0; padding: 0; box-sizing: border-box; }
  html, body {
    width: 1200px;
    height: 966px;
    overflow: hidden;
    background: var(--page-bg);
  }
  .canvas {
    position: relative;
    width: 1200px;
    height: 966px;
  }
  .card {
    position: absolute;
    left: 276px;
    width: 687px;
    background: var(--card-red);
    box-shadow: 6px 7px 8px var(--card-shadow);
    overflow: hidden;
    color: var(--card-white);
    font-family: "Questrial", "Century Gothic", sans-serif;
  }
  .card--front { top: 60px; height: 390px; }
  .card--back { top: 503px; height: 387px; }

  /* Front */
  .tagline-panel {
    position: absolute;
    right: 0;
    top: 0;
    width: 248px;
    height: 250px;
    background: var(--card-black);
    box-shadow: -4px 4px 6px rgba(0,0,0,0.35);
  }
  .tagline-strip {
    position: absolute;
    right: 0;
    top: 250px;
    width: 226px;
    height: 16px;
    background: var(--card-white);
  }
  .tagline {
    position: absolute;
    left: 30px;
    top: 72px;
    font-size: 26px;
    line-height: 32.5px;
    letter-spacing: 0.3px;
  }
  .wordmark {
    position: absolute;
    display: flex;
    align-items: center;
    gap: 16px;
    font-size: 50px;
    line-height: 1;
    color: var(--card-white);
    white-space: nowrap;
  }
  .wordmark__dot {
    width: 22px;
    height: 22px;
    border-radius: 50%;
    background: var(--card-white);
    flex: none;
  }
  .card--front .wordmark { left: 36px; top: 298px; }

  /* Back */
  .contact-band {
    position: absolute;
    left: 0; top: 0;
    width: 100%;
    height: 123px;
    background: var(--card-black);
    text-align: center;
    padding-top: 37px;
    font-size: 20px;
    line-height: 26px;
    letter-spacing: 0.3px;
  }
  .contact-strip {
    position: absolute;
    left: 0; top: 123px;
    width: 100%;
    height: 14px;
    background: var(--card-white);
  }
  .person {
    position: absolute;
    left: 395px;
    top: 159px;
    font-family: "Mulish", "Verdana", sans-serif;
  }
  .person__name { font-size: 24px; font-weight: 700; line-height: 30px; }
  .person__role { font-size: 17px; font-style: italic; line-height: 22px; }
  .person__phone { font-size: 19px; margin-top: 20px; letter-spacing: 0.4px; }
  .card--back .wordmark { left: 36px; top: 302px; font-size: 46px; }
</style>
</head>
<body>
<main class="canvas">
  <section class="card card--front" aria-label="Card front">
    <div class="tagline-panel">
      <p class="tagline">Discreet<br>Surveillance<br>Equipment</p>
    </div>
    <div class="tagline-strip"></div>
    <div class="wordmark">
      <span class="wordmark__dot" aria-hidden="true"></span>
      <span class="wordmark__name">Brisk Lantern</span>
    </div>
  </section>

  <section class="card card--back" aria-label="Card back">
    <div class="contact-band">
      <p class="contact-email">harold.dumbrell@brisklantern.example</p>
      <p class="contact-web">www.brisklantern.example</p>
    </div>
    <div class="contact-strip"></div>
    <div class="person">
      <p class="person__name">Harold Dumbrell</p>
      <p class="person__role">Consultant</p>
      <p class="person__phone">555-318-0927</p>
    </div>
    <div class="wordmark">
      <span class="wordmark__dot" aria-hidden="true"></span>
      <span class="wordmark__name">Brisk Lantern, Inc.</span>
    </div>
  </section>
</main>
</body>
</html>
```